Boutique Store Selling Antiques and Unique Finds

I need a Web Page designed for my Store Called "Harrow Lane". I would like a very classic, muted design that looks European when pulled up. I will be selling Antiques from all over the world and Unique finds that have reproduced. I will also be selling high-end purses and jewelry with unique, reasonable products for the every-day buyer as well.

Target Market(s)

25-70 year old men and women;)

Coding

Number of Pages Required

1 page

Colors

Designer to choose only greyscale colors for use in the design.

Requirements
Must have
• I want it

```html
<!DOCTYPE html>
<html lang="en">
<head>
<meta charset="utf-8">
<title>Harrow Lane — Home Page Variants</title>
<link href="https://fonts.googleapis.com/css2?family=Cinzel:wght@600&family=Lora:wght@400;500&family=Montserrat:wght@400;500&family=Open+Sans:wght@400;600&display=swap" rel="stylesheet">
<style>
:root{
  --canvas:#f2f2f2;
  --white:#ffffff;
  --bar:#f3f3f3;
  --ink:#2b2b2b;
  --ink-soft:#555555;
  --muted:#8a8a8a;
  --line:#d9d9d9;
  --section:#f6f6f6;
  --footer:#262626;
  --footer-base:#1f1f1f;
  --footer-chip:#3a3a3a;
  --footer-text:#e8e8e8;
}
*{margin:0;padding:0;box-sizing:border-box}
html,body{width:1114px;height:1200px;overflow:hidden;background:var(--canvas)}
body{position:relative;font-family:"Lora",serif;color:var(--ink)}
.page{position:absolute;width:520px;background:var(--white);box-shadow:0 0 4px rgba(0,0,0,.12);overflow:hidden}
.page--classic{left:27px;top:51px;height:1005px}
.page--modern{left:570px;top:49px;height:1104px}
.abs{position:absolute}

/* header */
.utility-bar{left:0;top:0;width:520px;height:23px;background:var(--bar);border-bottom:1px solid #e4e4e4;font-size:6.5px;color:var(--ink-soft)}
.utility-bar span{position:absolute;top:8px}
.header-brand{left:0;width:520px;font-family:"Cinzel",serif;font-weight:600;color:var(--ink);letter-spacing:2px;white-space:nowrap;text-align:center;font-size:13px}
.page--classic .header-brand{top:46px}
.page--modern .header-brand{top:29px}
.header-rule{left:48px;top:72px;width:423px;height:1px;background:var(--line)}
.main-nav{font-size:6.3px;color:var(--ink);white-space:nowrap;text-transform:uppercase}
.main-nav span{position:absolute}
.hero-classic{left:0;top:101px;width:520px;height:301px;background:radial-gradient(ellipse at 50% 45%,#a0814e 0%,#7a6141 35%,#5a4734 70%,#3f342a 100%)}
.hero-classic h1{position:absolute;left:0;width:520px;top:124px;text-align:center;font-family:"Lora",serif;font-weight:500;color:var(--white);font-size:17.5px;line-height:23px;letter-spacing:.3px}
.dots{left:250px;top:392px;display:flex;gap:4px}
.dots i{width:4.5px;height:4.5px;border-radius:50%;background:var(--white);display:block}
.dots i.on{background:#6fa3d6}

/* products */
.products{left:0;width:520px;background:var(--section)}
.section-title{position:absolute;left:0;width:520px;text-align:center;font-size:17px;font-weight:400;color:var(--ink-soft)}
.title-rule{position:absolute;left:251px;width:18px;height:1px;background:var(--ink-soft)}
.card{position:absolute;width:99px;height:156px;background:var(--white);box-shadow:0 0 3px rgba(0,0,0,.08)}
.card .photo{position:absolute;left:4px;top:4px;width:91px;height:80px}
.card .price{position:absolute;left:0;width:99px;top:94px;text-align:center;font-size:9px;color:var(--ink)}
.card .name{position:absolute;left:0;width:99px;top:110px;text-align:center;font-size:7.3px;color:var(--ink-soft)}
.card .details{position:absolute;left:20px;top:126px;width:59px;height:19px;border:1px solid var(--line);border-radius:10px;text-align:center;line-height:17px;font-size:6.5px;color:var(--ink-soft)}

.ph-cases{background:linear-gradient(180deg,#8a7a52 0%,#5f7ca0 45%,#3a2a22 100%)}
.ph-stairs{background:linear-gradient(135deg,#6b3f24 0%,#3e2416 60%,#8a7a64 100%)}
.ph-shelf{background:linear-gradient(135deg,#b89c6e 0%,#5a4a3a 55%,#2c2a30 100%)}
.ph-medal{background:radial-gradient(circle at 50% 55%,#6b6658 0%,#cbbba2 45%,#d6c8b2 100%)}
.ph-books{background:linear-gradient(90deg,#4a2a1e 0%,#6a2828 35%,#2a1e1a 65%,#5a3a26 100%)}
.ph-statue{background:linear-gradient(135deg,#5a3622 0%,#b8a68c 50%,#6b4a30 100%)}
.ph-plant{background:radial-gradient(circle at 50% 50%,#3e5a2e 0%,#2c3f22 55%,#c9c4b8 100%)}
.ph-hat{background:linear-gradient(180deg,#c8c2b6 0%,#2a2420 45%,#6a6258 75%,#3a3028 100%)}

/* footer */
.footer{left:0;width:520px;height:142px;background:var(--footer);font-family:"Montserrat",sans-serif;color:var(--footer-text)}
.footer-brand{position:absolute;left:48px;width:115px;top:57px;font-family:"Cinzel",serif;font-weight:600;font-size:10.5px;color:var(--white);letter-spacing:1.6px;white-space:nowrap;text-align:center}
.social{position:absolute;width:15px;height:15px;border:1px solid #cfcfcf;border-radius:50%;top:80px}
.footer h3{position:absolute;top:24px;font-family:"Montserrat",sans-serif;font-weight:500;font-size:9px;color:var(--white);letter-spacing:.2px}
.quick-links{position:absolute;left:189px;top:42px;list-style:none;font-size:5.2px;text-transform:uppercase;line-height:13px}
.quick-links li{display:flex;align-items:center;gap:5px}
.quick-links svg{width:7px;height:4px}
.contact-item{position:absolute;left:293px;font-size:6.2px;line-height:10.2px}
.chip{position:absolute;left:272px;width:15px;height:15px;border-radius:50%;background:var(--footer-chip);display:flex;align-items:center;justify-content:center}
.chip svg{width:7px;height:7px}
.pay-note{position:absolute;left:380px;top:45px;font-size:5.6px;line-height:10.4px;width:110px}
.pay-badges{position:absolute;left:380px;top:75px;display:flex;gap:1.5px}
.pay-badges i{display:block;width:17px;height:11px;border-radius:1.5px;background:#f4f4f4}
.footer-base{left:0;width:520px;height:29px;background:var(--footer-base);font-family:"Montserrat",sans-serif;font-size:6.3px;color:var(--footer-text);text-align:center;line-height:29px}

/* modern variant */
.account-links{font-family:"Open Sans",sans-serif;font-size:5.6px;color:var(--muted)}
.hero-modern{left:0;top:76px;width:520px;height:223px;background:linear-gradient(90deg,#3a3a3a 0%,#4a4a4a 45%,#555555 100%)}
.hero-modern .chair{position:absolute;left:238px;top:40px;width:164px;height:183px;background:radial-gradient(ellipse at 50% 50%,#6f705e 0%,#5a5a48 45%,#8a7040 70%,rgba(74,74,74,0) 100%)}
.hero-modern .floor{position:absolute;left:0;top:180px;width:520px;height:43px;background:linear-gradient(180deg,#6a6a6a 0%,#5a4e42 60%,#4a3e34 100%)}
.hero-copy{position:absolute;left:51px;font-family:"Open Sans",sans-serif;color:var(--white)}
.hero-copy h2{position:absolute;left:0;top:0;white-space:nowrap;font-weight:400;font-size:16px;letter-spacing:.4px}
.hero-copy p{position:absolute;left:0;top:26px;width:170px;font-size:6.7px;line-height:10.3px;letter-spacing:.2px}
.shop-now{position:absolute;left:1px;top:56px;width:95px;height:21px;border-radius:11px;background:var(--white);color:var(--ink);font-size:6.5px;font-weight:600;text-align:center;line-height:21px;letter-spacing:.4px}
.slide-arrow{position:absolute;width:27px;height:27px;border:1px solid #d8d8d8;border-radius:50%;top:101px;display:flex;align-items:center;justify-content:center}
.slide-arrow svg{width:10px;height:8px}
.feature{left:0;top:719px;width:520px;height:214px;background:linear-gradient(90deg,#6a5634 0%,#a08a62 30%,#cfc1a6 55%,#d9ccb4 100%)}
.feature .crown-photo{position:absolute;left:0;top:0;width:250px;height:214px;background:radial-gradient(ellipse at 45% 50%,#8a6a32 0%,#5a4526 45%,rgba(160,138,98,0) 80%)}
.feature h2{position:absolute;left:271px;top:54px;font-weight:400;font-size:16px;color:var(--ink-soft);white-space:nowrap}
.feature p{position:absolute;left:271px;top:79px;width:176px;font-family:"Open Sans",sans-serif;font-size:5.5px;line-height:11.1px;color:var(--ink-soft);text-align:justify}
</style>
</head>
<body>

<!-- Classic variant -->
<section class="page page--classic">
  <div class="abs utility-bar">
    <span style="left:48px">My Account</span>
    <span style="left:93px">|</span>
    <span style="left:106px">Check Out</span>
    <span style="left:400px">Sign in</span>
    <span style="left:429px">&#9633; Cart (0)</span>
    <svg class="abs" style="left:466px;top:8px" width="7" height="7" viewBox="0 0 10 10"><circle cx="4" cy="4" r="3" fill="none" stroke="#444" stroke-width="1.4"/><path d="M6.2 6.2L9 9" stroke="#444" stroke-width="1.4"/></svg>
  </div>
  <div class="abs header-brand">Harrow Lane</div>
  <div class="abs header-rule"></div>
  <nav class="abs main-nav" style="left:0;top:83px;width:520px">
    <span style="left:67px">Home</span>
    <span style="left:105px">About Us</span>
    <span style="left:155px">Antique &amp; Unique</span>
    <span style="left:235px">Crowns</span>
    <span style="left:281px">Home Goods</span>
    <span style="left:343px">Jewelry</span>
    <span style="left:390px">Handbags &amp; Shoes</span>
  </nav>
  <div class="abs hero-classic" role="img" aria-label="Photo of an antique gilded crown with star points on a dark pedestal">
    <h1>ANTIQUE AND UNIQUE<br>FINDS FROM AROUND THE WORLD</h1>
  </div>
  <div class="abs dots"><i></i><i class="on"></i><i></i></div>

  <div class="abs products" style="top:402px;height:432px">
    <h2 class="section-title" style="top:20px">Our Products</h2>
    <div class="title-rule" style="top:45px"></div>

    <article class="card" style="left:49px;top:59px"><div class="photo ph-cases" role="img" aria-label="Stacked vintage suitcases beneath a potted plant"></div><div class="price">$25.99</div><div class="name">Product Name</div><div class="details">View Details</div></article>
    <article class="card" style="left:157px;top:59px"><div class="photo ph-stairs" role="img" aria-label="Wood-panelled hall with staircase and carved figure"></div><div class="price">$25.99</div><div class="name">Product Name</div><div class="details">View Details</div></article>
    <article class="card" style="left:264px;top:59px"><div class="photo ph-shelf" role="img" aria-label="Shelf of assorted vintage hats and boxes"></div><div class="price">$25.99</div><div class="name">Product Name</div><div class="details">View Details</div></article>
    <article class="card" style="left:372px;top:59px"><div class="photo ph-medal" role="img" aria-label="Antique bronze medal on a ribbon"></div><div class="price">$25.99</div><div class="name">Product Name</div><div class="details">View Details</div></article>

    <article class="card" style="left:49px;top:239px"><div class="photo ph-books" role="img" aria-label="Row of leather-bound antique books"></div><div class="price">$25.99</div><div class="name">Product Name</div><div class="details">View Details</div></article>
    <article class="card" style="left:157px;top:239px"><div class="photo ph-statue" role="img" aria-label="Carved stone statue in a wooden hall"></div><div class="price">$25.99</div><div class="name">Product Name</div><div class="details">View Details</div></article>
    <article class="card" style="left:264px;top:239px"><div class="photo ph-plant" role="img" aria-label="Leafy potted plant in a metal bowl"></div><div class="price">$25.99</div><div class="name">Product Name</div><div class="details">View Details</div></article>
    <article class="card" style="left:372px;top:239px"><div class="photo ph-hat" role="img" aria-label="Fur crown hat resting on stacked books"></div><div class="price">$25.99</div><div class="name">Product Name</div><div class="details">View Details</div></article>
  </div>

  <footer class="abs footer" style="top:834px">
    <div class="footer-brand">Harrow Lane</div>
    <i class="social" style="left:61px"></i><i class="social" style="left:80px"></i><i class="social" style="left:98px"></i><i class="social" style="left:117px"></i><i class="social" style="left:136px"></i>
    <h3 style="left:189px">QUICK LINKS</h3>
    <ul class="quick-links">
      <li><svg viewBox="0 0 14 8"><path d="M0 4h12M9 1l3 3-3 3" fill="none" stroke="#ddd" stroke-width="1"/></svg>Home</li>
      <li><svg viewBox="0 0 14 8"><path d="M0 4h12M9 1l3 3-3 3" fill="none" stroke="#ddd" stroke-width="1"/></svg>About Us</li>
      <li><svg viewBox="0 0 14 8"><path d="M0 4h12M9 1l3 3-3 3" fill="none" stroke="#ddd" stroke-width="1"/></svg>Antique &amp; Unique</li>
      <li><svg viewBox="0 0 14 8"><path d="M0 4h12M9 1l3 3-3 3" fill="none" stroke="#ddd" stroke-width="1"/></svg>Crowns</li>
      <li><svg viewBox="0 0 14 8"><path d="M0 4h12M9 1l3 3-3 3" fill="none" stroke="#ddd" stroke-width="1"/></svg>Home Goods</li>
      <li><svg viewBox="0 0 14 8"><path d="M0 4h12M9 1l3 3-3 3" fill="none" stroke="#ddd" stroke-width="1"/></svg>Jewelry</li>
      <li><svg viewBox="0 0 14 8"><path d="M0 4h12M9 1l3 3-3 3" fill="none" stroke="#ddd" stroke-width="1"/></svg>Handbags &amp; Shoes</li>
    </ul>
    <h3 style="left:273px">CONTACT US</h3>
    <div class="chip" style="top:44px"><svg viewBox="0 0 10 10"><path d="M2 1l2 2-1 1.5c.6 1.2 1.3 1.9 2.5 2.5L7 6l2 2-1.2 1.2C4.5 9 1 5.5.8 2.2z" fill="#fff"/></svg></div>
    <div class="contact-item" style="top:47px">000-121-1231</div>
    <div class="chip" style="top:66px"><svg viewBox="0 0 10 10"><rect x="1" y="2" width="8" height="6" fill="none" stroke="#fff" stroke-width="1"/><path d="M1 2l4 3.5L9 2" fill="none" stroke="#fff" stroke-width="1"/></svg></div>
    <div class="contact-item" style="top:68px">info@company.com</div>
    <div class="chip" style="top:87px"><svg viewBox="0 0 10 10"><path d="M5 9.5S2 6 2 4a3 3 0 016 0c0 2-3 5.5-3 5.5z" fill="#fff"/><circle cx="5" cy="4" r="1" fill="#3a3a3a"/></svg></div>
    <div class="contact-item" style="top:87px">2172 Lorem Ipsum<br>dummy text 32308</div>
    <h3 style="left:380px">PAYMENTS</h3>
    <p class="pay-note">Sed ut perspiciatis unde omnis us<br>error sit voluptatem</p>
    <div class="pay-badges"><i></i><i></i><i></i><i></i><i></i></div>
  </footer>
  <div class="abs footer-base" style="top:976px">© Copyrights 2021-Harrow Lane.All Rights Reserved.</div>
</section>

<!-- Modern variant -->
<section class="page page--modern">
  <div class="abs account-links" style="left:366px;top:10px">Sign in or Register</div>
  <svg class="abs" style="left:430px;top:10px" width="8" height="7" viewBox="0 0 12 10"><path d="M0 1h2l2 6h6l1.5-4.5H3" fill="none" stroke="#777" stroke-width="1"/><circle cx="5" cy="9" r=".8" fill="#777"/><circle cx="9" cy="9" r=".8" fill="#777"/></svg>
  <div class="abs account-links" style="left:439px;top:10px">(0) Items</div>
  <svg class="abs" style="left:465px;top:11px" width="6" height="6" viewBox="0 0 10 10"><circle cx="4" cy="4" r="3" fill="none" stroke="#444" stroke-width="1.4"/><path d="M6.2 6.2L9 9" stroke="#444" stroke-width="1.4"/></svg>
  <div class="abs header-brand">Harrow Lane</div>
  <nav class="abs main-nav" style="left:0;top:55px;width:520px">
    <span style="left:61px;color:var(--muted)">Home</span>
    <span style="left:102px">About Us</span>
    <span style="left:155px">Antique &amp; Unique</span>
    <span style="left:237px">Crowns</span>
    <span style="left:286px">Home Goods</span>
    <span style="left:351px">Jewelry</span>
    <span style="left:401px">Andbags &amp; Shoes</span>
  </nav>

  <div class="abs hero-modern">
    <div class="floor" role="img" aria-label="Polished wooden floor and skirting"></div>
    <div class="chair" role="img" aria-label="Ornate gilded armchair with tufted velvet upholstery"></div>
    <div class="slide-arrow" style="left:13px"><svg viewBox="0 0 12 10"><path d="M11 5H1M5 1L1 5l4 4" fill="none" stroke="#fff" stroke-width="1.2"/></svg></div>
    <div class="slide-arrow" style="left:480px"><svg viewBox="0 0 12 10"><path d="M1 5h10M7 1l4 4-4 4" fill="none" stroke="#fff" stroke-width="1.2"/></svg></div>
    <div class="hero-copy" style="top:77px">
      <h2>HARROW LANE</h2>
      <p>Sed ut perspiciatis unde omnis iste natus error sit voluptatem accusantium</p>
      <div class="shop-now">SHOP NOW</div>
    </div>
  </div>

  <div class="abs products" style="top:299px;height:420px">
    <h2 class="section-title" style="top:12px">Our Products</h2>
    <div class="title-rule" style="top:37px"></div>

    <article class="card" style="left:49px;top:52px"><div class="photo ph-cases" role="img" aria-label="Stacked vintage suitcases beneath a potted plant"></div><div class="price">$25.99</div><div class="name">Product Name</div><div class="details">View Details</div></article>
    <article class="card" style="left:157px;top:52px"><div class="photo ph-stairs" role="img" aria-label="Wood-panelled hall with staircase and carved figure"></div><div class="price">$25.99</div><div class="name">Product Name</div><div class="details">View Details</div></article>
    <article class="card" style="left:264px;top:52px"><div class="photo ph-shelf" role="img" aria-label="Shelf of assorted vintage hats and boxes"></div><div class="price">$25.99</div><div class="name">Product Name</div><div class="details">View Details</div></article>
    <article class="card" style="left:371px;top:52px"><div class="photo ph-medal" role="img" aria-label="Antique bronze medal on a ribbon"></div><div class="price">$25.99</div><div class="name">Product Name</div><div class="details">View Details</div></article>

    <article class="card" style="left:49px;top:231px"><div class="photo ph-books" role="img" aria-label="Row of leather-bound antique books"></div><div class="price">$25.99</div><div class="name">Product Name</div><div class="details">View Details</div></article>
    <article class="card" style="left:157px;top:231px"><div class="photo ph-statue" role="img" aria-label="Carved stone statue in a wooden hall"></div><div class="price">$25.99</div><div class="name">Product Name</div><div class="details">View Details</div></article>
    <article class="card" style="left:264px;top:231px"><div class="photo ph-plant" role="img" aria-label="Leafy potted plant in a metal bowl"></div><div class="price">$25.99</div><div class="name">Product Name</div><div class="details">View Details</div></article>
    <article class="card" style="left:371px;top:231px"><div class="photo ph-hat" role="img" aria-label="Fur crown hat resting on stacked books"></div><div class="price">$25.99</div><div class="name">Product Name</div><div class="details">View Details</div></article>
  </div>

  <div class="abs feature">
    <div class="crown-photo" role="img" aria-label="Jewelled antique crown against a damask wall"></div>
    <h2>Antiques &amp; Unique Finds</h2>
    <p>Sed ut perspiciatis unde omnis iste natus error sit voluptatem accusantium doloremque laudantium, totam rem aperiam, eaque ipsa quae ab illo inventore veritatis et quasi architecto beatae vitae dicta sunt explicabo. Nemo enim ipsam voluptatem quia voluptas sit aspernatur aut odit aut fugit, sed quia consequuntur magni dolores eos qui ratione voluptatem sequi nesciunt.</p>
  </div>

  <footer class="abs footer" style="top:933px">
    <div class="footer-brand">Harrow Lane</div>
    <i class="social" style="left:61px"></i><i class="social" style="left:80px"></i><i class="social" style="left:98px"></i><i class="social" style="left:117px"></i><i class="social" style="left:136px"></i>
    <h3 style="left:189px">QUICK LINKS</h3>
    <ul class="quick-links">
      <li><svg viewBox="0 0 14 8"><path d="M0 4h12M9 1l3 3-3 3" fill="none" stroke="#ddd" stroke-width="1"/></svg>Home</li>
      <li><svg viewBox="0 0 14 8"><path d="M0 4h12M9 1l3 3-3 3" fill="none" stroke="#ddd" stroke-width="1"/></svg>About Us</li>
      <li><svg viewBox="0 0 14 8"><path d="M0 4h12M9 1l3 3-3 3" fill="none" stroke="#ddd" stroke-width="1"/></svg>Antique &amp; Unique</li>
      <li><svg viewBox="0 0 14 8"><path d="M0 4h12M9 1l3 3-3 3" fill="none" stroke="#ddd" stroke-width="1"/></svg>Crowns</li>
      <li><svg viewBox="0 0 14 8"><path d="M0 4h12M9 1l3 3-3 3" fill="none" stroke="#ddd" stroke-width="1"/></svg>Home Goods</li>
      <li><svg viewBox="0 0 14 8"><path d="M0 4h12M9 1l3 3-3 3" fill="none" stroke="#ddd" stroke-width="1"/></svg>Jewelry</li>
      <li><svg viewBox="0 0 14 8"><path d="M0 4h12M9 1l3 3-3 3" fill="none" stroke="#ddd" stroke-width="1"/></svg>Handbags &amp; Shoes</li>
    </ul>
    <h3 style="left:273px">CONTACT US</h3>
    <div class="chip" style="top:44px"><svg viewBox="0 0 10 10"><path d="M2 1l2 2-1 1.5c.6 1.2 1.3 1.9 2.5 2.5L7 6l2 2-1.2 1.2C4.5 9 1 5.5.8 2.2z" fill="#fff"/></svg></div>
    <div class="contact-item" style="top:47px">000-121-1231</div>
    <div class="chip" style="top:66px"><svg viewBox="0 0 10 10"><rect x="1" y="2" width="8" height="6" fill="none" stroke="#fff" stroke-width="1"/><path d="M1 2l4 3.5L9 2" fill="none" stroke="#fff" stroke-width="1"/></svg></div>
    <div class="contact-item" style="top:68px">info@company.com</div>
    <div class="chip" style="top:87px"><svg viewBox="0 0 10 10"><path d="M5 9.5S2 6 2 4a3 3 0 016 0c0 2-3 5.5-3 5.5z" fill="#fff"/><circle cx="5" cy="4" r="1" fill="#3a3a3a"/></svg></div>
    <div class="contact-item" style="top:87px">2172 Lorem Ipsum<br>dummy text 32308</div>
    <h3 style="left:380px">PAYMENTS</h3>
    <p class="pay-note">Sed ut perspiciatis unde omnis us<br>error sit voluptatem</p>
    <div class="pay-badges"><i></i><i></i><i></i><i></i><i></i></div>
  </footer>
  <div class="abs footer-base" style="top:1075px">© Copyrights 2021-Harrow Lane.All Rights Reserved.</div>
</section>

</body>
</html>
```